DL Flyer for garden consultants. I will supply text and logo

To design an eye catching but simple, uncluttered flyer for letter box distribution. The text and logo are provided.

```html
<!DOCTYPE html>
<html lang="en">
<head>
<meta charset="utf-8">
<title>Leafwise Garden Consultants – DL Flyer</title>
<link rel="stylesheet" href="https://fonts.googleapis.com/css2?family=Nunito:wght@600;700;800&display=swap">
<style>
  :root {
    --stage: #e4e4e4;
    --lime: #bcd90a;
    --lime-deep: #a9cc0c;
    --lime-band: #d0e84f;
    --green: #2e9140;
    --green-light: #7ab51d;
    --forest: #1e3b2a;
    --white: #ffffff;
  }
  * { box-sizing: border-box; margin: 0; padding: 0; }
  html, body { width: 1200px; height: 849px; overflow: hidden; }
  body {
    background: var(--stage);
    font-family: "Nunito", sans-serif;
    position: relative;
  }
  .flyer {
    position: absolute;
    width: 658px;
    height: 314px;
    overflow: hidden;
  }
  .flyer--front {
    left: 182px; top: 98px;
    background: linear-gradient(180deg, var(--lime) 0%, var(--lime-deep) 100%);
  }
  .flyer--back {
    left: 401px; top: 440px;
    background: var(--white);
  }
  .line { position: absolute; white-space: nowrap; font-weight: 800; }

  /* front */
  .question { left: 144px; top: 46px; font-size: 26px; color: var(--green); }
  .headline { left: 120px; top: 106px; color: var(--forest); line-height: 1; }
  .headline .small { font-size: 38px; }
  .headline .big { font-size: 48px; }
  .lately { left: 122px; top: 186px; font-size: 24px; color: var(--green); }
  .well { left: 324px; top: 184px; font-size: 34px; color: var(--forest); }
  .url-band {
    position: absolute; left: 0; right: 0; top: 250px; height: 38px;
    background: var(--lime-band);
    display: flex; align-items: center; justify-content: center;
    font-weight: 800; font-size: 23px; color: var(--forest);
  }

  /* back */
  .brand { position: absolute; left: 32px; top: 30px; display: flex; align-items: center; gap: 10px; }
  .brand-dot { width: 34px; height: 34px; border-radius: 50%; background: var(--green); }
  .brand-text { color: var(--green); font-weight: 800; line-height: 1.05; }
  .brand-name { font-size: 34px; }
  .brand-sub { font-size: 11px; letter-spacing: 2px; }
  .help { left: 246px; top: 68px; font-size: 26px; color: var(--forest); }
  .services { position: absolute; left: 42px; top: 124px; list-style: none; }
  .service { position: relative; padding-left: 22px; margin-bottom: 14px; }
  .service::before {
    content: ""; position: absolute; left: 0; top: 5px;
    width: 12px; height: 12px; border-radius: 50%; background: var(--green-light);
  }
  .service-title { font-size: 13px; font-weight: 800; color: var(--forest); }
  .service-note { font-size: 12px; font-weight: 700; color: var(--green-light); padding-left: 8px; }
  .visit { left: 32px; top: 268px; font-size: 17px; color: var(--forest); }
  .visit a { color: var(--green-light); text-decoration: none; }
</style>
</head>
<body>
  <section class="flyer flyer--front" aria-label="Flyer front">
    <p class="line question">HAVE YOU BEEN THINKING ABOUT</p>
    <p class="line headline"><span class="small">YOUR</span> <span class="big">GARDEN</span></p>
    <p class="line lately">LATELY?</p>
    <p class="line well">Well.........</p>
    <div class="url-band">www.leafwisegardens.com.au</div>
  </section>

  <section class="flyer flyer--back" aria-label="Flyer back">
    <div class="brand">
      <span class="brand-dot"></span>
      <div class="brand-text">
        <div class="brand-name">Leafwise</div>
        <div class="brand-sub">GARDEN CONSULTANTS</div>
      </div>
    </div>
    <p class="line help">......... we can help.</p>
    <ul class="services">
      <li class="service">
        <div class="service-title">Garden Assessment Consultation and Report</div>
        <div class="service-note">...... information vital to ensuring your dream becomes reality!</div>
      </li>
      <li class="service">
        <div class="service-title">Pre Sale Consultation and Report</div>
        <div class="service-note">.....  maximise your sale dollar!</div>
      </li>
      <li class="service">
        <div class="service-title">Develop a Plant Portfolio</div>
        <div class="service-note">..... successfully navigate the plant maze!</div>
      </li>
    </ul>
    <p class="line visit">Check us out at <a href="#">www.leafwisegardens.com.au</a></p>
  </section>
</body>
</html>
```